UNIQUE, Elegant business card for transport company.

MUST BE AN ACTUAL GRAPHIC DESIGNER.
NO TEMPLATES, NO MOCKUP GENERATORS.
Looking for a top notch, head turning, business card.
Will be printed on premium luxury paper with spot glossing and debossing.
Must know how to set up for spot glossing. Must be willing to work on the file to meet printers spec after final design.

Target Market(s)

All info on .psd file

Contact Information for Business Card

All info on .psd file

Requirements
Must have
• All info on .psd file
Nice to have
• All info on .psd file
Should not have
• Nothing red

```html
<!DOCTYPE html>
<html lang="en">
<head>
<meta charset="utf-8">
<title>Velora Transport – Business Card</title>
<link rel="stylesheet" href="https://fonts.googleapis.com/css2?family=Noto+Serif:wght@400;700&family=Source+Sans+3:wght@400&display=swap">
<style>
  :root {
    --backdrop: #b9b9b9;
    --paper: #ffffff;
    --brand-blue: #2b8fc6;
    --sky: #00a6e4;
    --ocean: #0a78b5;
    --navy: #061c5c;
    --ink: #141414;
  }
  * { box-sizing: border-box; margin: 0; padding: 0; }
  html, body {
    width: 1058px; height: 1200px; overflow: hidden;
    background: var(--backdrop);
  }
  .card {
    position: absolute; left: 158px; width: 745px; height: 447px;
    background: var(--paper); overflow: hidden;
    box-shadow: 0 4px 14px rgba(0,0,0,0.25);
  }
  .card--front { top: 114px; }
  .card--back { top: 617px; }
  .waves { position: absolute; left: 0; top: 0; width: 745px; height: 447px; }

  .company-name {
    position: absolute; left: 51px; top: 46px;
    font-family: "Noto Serif", serif; font-weight: 700;
    font-size: 38px; line-height: 41px; color: var(--brand-blue);
  }
  .contact-list { position: absolute; left: 52px; top: 162px; list-style: none; }
  .contact-list li {
    display: flex; align-items: center; height: 41px;
    font-family: "Source Sans 3", sans-serif; font-size: 21px; color: var(--ink);
  }
  .contact-list svg { width: 22px; height: 22px; margin-right: 9px; fill: var(--brand-blue); }

  .brand-mark {
    position: absolute; display: flex; flex-direction: column; align-items: center; gap: 8px;
    font-family: "Noto Serif", serif; font-weight: 700; font-size: 24px; color: var(--brand-blue);
  }
  .brand-mark__dot { width: 58px; height: 58px; border-radius: 50%; background: var(--brand-blue); }
  .card--front .brand-mark { left: 585px; top: 72px; }
  .card--back .brand-mark { left: 58px; top: 90px; font-size: 30px; }
  .card--back .brand-mark__dot { width: 72px; height: 72px; }

  .holder {
    position: absolute; right: 50px; top: 349px; text-align: right;
    font-family: "Noto Serif", serif; font-size: 26px; line-height: 25px; color: #fff;
  }

  .tagline {
    position: absolute; right: 48px; top: 42px; text-align: right;
    font-family: "Noto Serif", serif; font-weight: 700;
    font-size: 33px; line-height: 37px; color: var(--brand-blue);
  }
  .credentials {
    position: absolute; right: 53px; top: 137px;
    font-family: "Source Sans 3", sans-serif; font-size: 21px; color: var(--ink);
  }
  .details {
    position: absolute; right: 50px; top: 194px;
    display: grid; grid-template-columns: auto auto; column-gap: 26px; row-gap: 12px;
    font-family: "Source Sans 3", sans-serif; font-size: 21px; color: var(--ink); text-align: right;
  }
</style>
</head>
<body>

<section class="card card--front">
  <svg class="waves" viewBox="0 0 1056 634" preserveAspectRatio="none" aria-hidden="true">
    <defs>
      <linearGradient id="ribbon-front" x1="0" y1="0" x2="1" y2="0">
        <stop offset="0" stop-color="#00a6e4"/>
        <stop offset="0.5" stop-color="#0a78b5"/>
        <stop offset="1" stop-color="#00a6e4"/>
      </linearGradient>
    </defs>
    <path fill="url(#ribbon-front)" d="M0,530 C60,555 110,580 150,592 C300,640 480,630 710,488 C830,410 950,350 1056,335 L1056,634 L0,634 Z"/>
    <path fill="var(--navy)" d="M0,585 C150,595 400,560 710,488 C850,465 980,475 1056,492 L1056,634 L0,634 Z"/>
  </svg>

  <h1 class="company-name">VELORA TRANSPORT,<br>INC.</h1>

  <ul class="contact-list">
    <li><svg viewBox="0 0 24 24"><path d="M7 1h10a2 2 0 0 1 2 2v18a2 2 0 0 1-2 2H7a2 2 0 0 1-2-2V3a2 2 0 0 1 2-2zm0 3v14h10V4z"/></svg>(555) 214-6087</li>
    <li><svg viewBox="0 0 24 24"><path d="M6.6 10.8a15 15 0 0 0 6.6 6.6l2.2-2.2a1 1 0 0 1 1-.25 11 11 0 0 0 3.6.6 1 1 0 0 1 1 1V20a1 1 0 0 1-1 1A17 17 0 0 1 3 4a1 1 0 0 1 1-1h3.5a1 1 0 0 1 1 1c0 1.25.2 2.45.6 3.6a1 1 0 0 1-.25 1z"/></svg>(555) 318-4402</li>
    <li><svg viewBox="0 0 24 24"><path d="M2 5h20v14H2zm2 2v.5l8 5 8-5V7zm0 3v7h16v-7l-8 5z"/></svg>dana@veloratransport.com</li>
    <li><svg viewBox="0 0 24 24"><path d="M12 2a10 10 0 1 0 0 20 10 10 0 0 0 0-20zm6.9 9h-3a15 15 0 0 0-1.3-6 8 8 0 0 1 4.3 6zM12 4c.9 1.2 1.8 3.6 1.9 7h-3.8c.1-3.4 1-5.8 1.9-7zM9.4 5a15 15 0 0 0-1.3 6h-3a8 8 0 0 1 4.3-6zM5.1 13h3a15 15 0 0 0 1.3 6 8 8 0 0 1-4.3-6zM12 20c-.9-1.2-1.8-3.6-1.9-7h3.8c-.1 3.4-1 5.8-1.9 7zm2.6-1a15 15 0 0 0 1.3-6h3a8 8 0 0 1-4.3 6z"/></svg>www.veloratransport.com</li>
  </ul>

  <div class="brand-mark"><span class="brand-mark__dot"></span>Velora</div>

  <p class="holder">Dana Hollis<br>Transporter</p>
</section>

<section class="card card--back">
  <svg class="waves" viewBox="0 0 1056 634" preserveAspectRatio="none" aria-hidden="true">
    <defs>
      <linearGradient id="ribbon-back" x1="0" y1="0" x2="1" y2="0">
        <stop offset="0" stop-color="#00a6e4"/>
        <stop offset="0.45" stop-color="#0a78b5"/>
        <stop offset="1" stop-color="#00a6e4"/>
      </linearGradient>
    </defs>
    <path fill="url(#ribbon-back)" d="M0,325 C150,340 280,420 370,480 C550,530 750,620 930,592 C990,575 1030,550 1056,537 L1056,634 L0,634 Z"/>
    <path fill="var(--navy)" d="M0,490 C150,460 300,460 370,480 C550,530 750,610 930,585 C990,580 1030,585 1056,585 L1056,634 L0,634 Z"/>
  </svg>

  <div class="brand-mark"><span class="brand-mark__dot"></span>Velora</div>

  <h2 class="tagline">We Put Our Heart In<br>Your Transport</h2>
  <p class="credentials">Licensed. Bonded. &amp; Insured.</p>

  <div class="details">
    <span>(800) BOOK VTX</span><span>US DOT 1234567</span>
    <span>(800) 555-0148</span><span>MC # 7654321</span>
  </div>
</section>

</body>
</html>
```